business stationery for email layout
startup company
Simple
RT
Via G. Morelli, 17
26813 Codogno LO
Italy
Info@Tallimora.com
www.tallimora.com
minimalist, retail, fashion, technology, internet, innovative,one-step ahead, easy, intuitive, immediate, serious,credible
logo blue version
logo grey version
symbol blue version
symbol grey version

```html
<!DOCTYPE html>
<html lang="en">
<head>
<meta charset="utf-8">
<title>Tallimora business cards</title>
<link rel="stylesheet" href="https://fonts.googleapis.com/css2?family=Montserrat:wght@600&family=Open+Sans:wght@400;600&display=swap">
<style>
  :root {
    --backdrop: #6e4a36;
    --card: #ffffff;
    --brand-blue: #1f4fa8;
    --deep-blue: #1d2f8f;
    --mid-blue: #3266c2;
    --light-cyan: #5fc3e8;
    --ink: #222222;
    --figure-soft: #dfe8f3;
    --figure-deep: #3a5fbf;
  }
  * { margin: 0; padding: 0; box-sizing: border-box; }
  html, body { width: 1200px; height: 838px; overflow: hidden; }
  body {
    background: var(--backdrop);
    position: relative;
    font-family: "Open Sans", Arial, sans-serif;
  }
  .card {
    position: absolute;
    background: var(--card);
    border-radius: 22px;
    overflow: hidden;
    box-shadow: 0 6px 18px rgba(0,0,0,0.35);
  }
  .card--front { left: 58px; top: 43px; width: 578px; height: 365px; }
  .card--back { left: 540px; top: 432px; width: 593px; height: 372px; background: linear-gradient(135deg, #ffffff 40%, #e9ecef 100%); }

  .wordmark {
    position: absolute;
    font-family: "Montserrat", Arial, sans-serif;
    font-weight: 600;
    color: var(--brand-blue);
    letter-spacing: 1px;
  }
  .card--front .wordmark { left: 24px; top: 42px; font-size: 40px; }
  .card--back .wordmark { left: 276px; top: 260px; font-size: 34px; }

  .initials {
    position: absolute; left: 32px; top: 164px;
    font-size: 28px; color: var(--ink);
  }
  .figure-area {
    position: absolute;
  }
  .card--front .figure-area {
    left: 360px; top: 0; width: 210px; height: 150px;
    background: radial-gradient(ellipse at center, var(--figure-soft) 0%, rgba(223,232,243,0) 70%);
  }
  .card--back .figure-area {
    left: -36px; top: 24px; width: 264px; height: 288px;
    background: radial-gradient(ellipse at 50% 50%, var(--figure-deep) 0%, rgba(58,95,191,0.5) 40%, rgba(58,95,191,0) 72%);
  }
  .wave { position: absolute; left: 0; top: 0; width: 578px; height: 365px; }

  .contact {
    position: absolute; left: 410px; top: 236px;
    font-size: 12.5px; line-height: 17px; color: #ffffff;
  }
  .contact .gap { height: 12px; }
  .website {
    position: absolute; left: 38px; top: 330px;
    font-size: 13px; color: #ffffff;
  }
</style>
</head>
<body>
  <section class="card card--front">
    <div class="figure-area" role="img" aria-label="Faint silhouette of a jumping shopper with a bag"></div>
    <svg class="wave" viewBox="0 0 578 365" aria-hidden="true">
      <defs>
        <linearGradient id="waveFill" x1="0" y1="1" x2="1" y2="0">
          <stop offset="0" stop-color="#1d2f8f"/>
          <stop offset="1" stop-color="#3a78cc"/>
        </linearGradient>
      </defs>
      <path d="M0,222 C140,262 300,222 410,178 C490,148 545,146 578,152 L578,140 C540,132 480,136 400,168 C290,212 140,250 0,210 Z" fill="#5fc3e8"/>
      <path d="M0,232 C140,272 300,232 410,188 C490,158 545,156 578,162 L578,365 L0,365 Z" fill="url(#waveFill)"/>
    </svg>
    <div class="wordmark">Tallimora</div>
    <div class="initials">RT</div>
    <div class="contact">
      <div>Via G. Morelli, 17</div>
      <div>26813 Codogno LO</div>
      <div>Italy</div>
      <div class="gap"></div>
      <div>P : +390200418263</div>
      <div>F : +390200418290</div>
      <div>E : Info@Tallimora.com</div>
    </div>
    <div class="website">www.tallimora.com</div>
  </section>

  <section class="card card--back">
    <div class="figure-area" role="img" aria-label="Blue silhouette of a woman leaping with a shopping bag"></div>
    <div class="wordmark">Tallimora</div>
  </section>
</body>
</html>
```